Birch & Ember Website Design (Rustic/Western)

OVERVIEW
Birch & Ember Supply House (aka Birch & Ember) manufactures rustic / western furniture and décor for cabins, lodges, and ranches. We also offer a line of accessories to complement our product line.
WEB PAGE (www.BirchAndEmber.example)
We are looking for a new web page design to represent our mountain-style (log furniture) and country-style (barnwood furniture) product line. We would like to re-create our existing homepage with a similar style template for our product line.
Our website is currently under construction – a draft has been published as an example outline. We are currently using Plinkora.example for our online store.
THEME
The overall theme needs to appear rustic, yet elegant. Listed below are only suggestions, not requirements. Please use your own creativity.
* Photographs: We will use our own photographs, for now any photograph will suffice.
* Background Colors: dark brown (rgb 21-9-2), medium brown (rgb 39-17-4), light brown (rgb 72-34-3). White background is also an option.
* Font Colors: beige (rgb 233-164-118), gold (rgb 151-98-2)
• Mountain-Style Images: cabin, wildlife, mountains, fishing, wildlife, trees, etc.
* Mountain-Style Colors: hunter green
* Country-Style Images: western, ranch, barn, farm animals, horse buggies, horseshoes, etc.
* Country-Style Colors: maroon
Thanks to all who are participating.
Target Market(s)
Outdoor enthusiasts who enjoy mountain living or country living. Our primary target market is our local market and within a 100 mile radius of our location.
Industry/Entity Type
Construction
Requirements
Must have
- Rustic, yet elegant design.
Homepage and product template page for displaying each item.
Nice to have
- Source code and functionality is optional.
Mountain-Style theme to represent our collection of log furniture and décor suited for cabins and lodges. Suggested color: hunter green. Images may include cabin, wildlife, mountains, fishing, wildlife, trees, etc.
Country-Style theme to represent our collection of barnwood furniture and décor suited for farms and ranches. Suggested color: maroon. Images may include western, ranch, barn, farm animals, horse buggies, horseshoes, etc.

```html
<!DOCTYPE html>
<html lang="en">
<head>
<meta charset="utf-8">
<title>Birch & Ember Supply House</title>
<link href="https://fonts.googleapis.com/css2?family=Open+Sans:wght@400;600;700&family=Roboto+Condensed:wght@400;700&display=swap" rel="stylesheet">
<style>
:root{
  --black:#000;
  --orange:#c8651b;
  --orange-dark:#a94f12;
  --text:#222;
  --muted:#777;
  --line:#d6d6d6;
  --foot-text:#8a8a8a;
  --white:#fff;
}
*{box-sizing:border-box;margin:0;padding:0}
html,body{width:786px;height:1200px;overflow:hidden;background:var(--white);font-family:'Open Sans',sans-serif;color:var(--text)}
.page{position:relative;width:786px;height:1200px;overflow:hidden}
.abs{position:absolute}
.header{left:0;top:0;width:786px;height:139px;background:var(--black)}
.brand{left:48px;top:40px;width:150px;text-align:center;color:var(--white)}
.brand .mark{width:34px;height:34px;border-radius:50%;background:var(--orange);margin:0 auto 8px}
.brand .name{font-size:13px;font-weight:700;letter-spacing:1px}
.brand .url{font-size:5px;color:#bbb;margin-top:2px}
.contacts{right:49px;top:17px;display:flex;gap:20px;white-space:nowrap}
.contact{font-size:11px;color:#ccc;display:flex;align-items:center;gap:5px}
.cart{left:613px;top:55px;width:124px;height:28px;border:1px solid #444;display:flex;font-size:8.5px;color:#aaa;line-height:10px}
.cart .icon{width:33px;background:var(--orange);display:flex;align-items:center;justify-content:center}
.cart .label{padding:4px 0 0 10px}
.nav{top:106px;right:49px;display:flex;gap:15px;font-size:12px;color:#ccc;font-weight:600;white-space:nowrap}
.nav .active{color:var(--orange)}
.tile{overflow:hidden}
.tile .tag{position:absolute;left:0;top:24px;background:rgba(20,15,10,.85);color:var(--white);font-weight:700;font-size:14px;padding:4px 12px}
.hero-caption{left:234px;top:376px;color:var(--white);font-weight:700;font-size:17px;white-space:nowrap}
.dots{left:501px;top:403px;display:flex;gap:3px}
.dots span{width:6px;height:6px;border:1px solid #ddd;border-radius:50%}
.dots span:first-child{background:#ddd}
.promo{left:234px;top:447px;color:var(--white)}
.promo h3{font-size:14px;font-weight:700;line-height:17px}
.promo p{font-size:9px;margin-top:5px}
.heading{font-family:'Roboto Condensed',sans-serif;color:var(--orange);font-size:18px;font-weight:400;white-space:nowrap}
.rule{height:2px;background:#7a3d12;width:62px;margin-top:6px}
.search{left:48px;top:589px;width:167px;height:18px;border:1px solid #444;font-size:8px;font-style:italic;color:#999;display:flex;align-items:center;gap:7px;padding-left:6px}
.cats{left:48px;top:615px;width:167px;list-style:none}
.cats li{height:26.2px;border:1px solid var(--line);border-top:none;font-size:9px;color:#444;display:flex;align-items:center;justify-content:space-between;padding:0 15px 0 7px}
.cats li:first-child{background:var(--orange);color:var(--white);border-color:var(--orange);height:26px}
.cats li::after{content:"";border-left:5px solid currentColor;border-top:4px solid transparent;border-bottom:4px solid transparent;opacity:.7}
.intro{left:233px;top:585px;width:504px}
.intro .lead{font-size:13px;color:#222}
.intro p{font-size:8.5px;color:var(--muted);line-height:13.5px;margin-top:3px}
.btn{display:inline-block;background:var(--orange);color:var(--white);font-size:8.5px;padding:4px 7px}
.btn.grey{background:#6e6e6e}
.card{top:735px;width:160px;height:220px;border:1px solid var(--line);box-shadow:0 0 2px rgba(0,0,0,.15);padding:8px 7px}
.card .photo{height:118px}
.card h4{font-family:'Open Sans',sans-serif;font-size:13px;font-weight:700;color:#777;margin-top:4px}
.card.first h4{color:var(--orange)}
.card p{font-size:8.5px;color:#666;line-height:13.5px;margin:2px 0 10px}
.card.first p{color:#222}
.footer{left:0;top:983px;width:786px;height:186px;background:var(--black)}
.fcol{top:1006px}
.fcol h5{font-size:9.5px;font-weight:700;color:var(--orange);text-transform:uppercase;white-space:nowrap}
.fcol .rule{width:33px;height:1px;background:var(--orange);margin:5px 0 6px}
.fcol ul{list-style:none}
.fcol li{font-size:8.5px;color:var(--foot-text);height:20px;display:flex;align-items:center;gap:6px;white-space:nowrap}
.fcol li::before{content:"";width:4px;height:4px;border:1px solid #777}
.fcol li.on{color:var(--orange)}
.social{display:flex;gap:7px;margin-top:3px}
.social span{width:14px;height:14px;border-radius:50%;background:#555}
.fcontact{font-size:8.5px;color:#bbb;line-height:14px;white-space:nowrap}
.fcontact b{display:inline-block;width:31px}
.copy{left:0;top:1177px;width:786px;text-align:center;font-size:8px;color:#222}
</style>
</head>
<body>
<div class="page">
  <header class="abs header">
    <div class="abs brand"><div class="mark"></div><div class="name">BIRCH &amp; EMBER</div><div class="url">www.BirchAndEmber.example</div></div>
    <div class="abs contacts">
      <div class="contact"><svg width="10" height="12" viewBox="0 0 10 12"><path d="M2 1l2 2-1 2c1 2 2 3 3 3l1-1 2 2-1 2C4 12 0 7 1 2z" fill="#c8651b"/></svg>555.014.2290</div>
      <div class="contact"><svg width="13" height="9" viewBox="0 0 13 9"><rect x=".5" y=".5" width="12" height="8" fill="none" stroke="#c8651b"/><path d="M.5.5l6 4 6-4" fill="none" stroke="#c8651b"/></svg>info@birchember.example</div>
    </div>
    <div class="abs cart"><div class="icon"><svg width="18" height="14" viewBox="0 0 18 14"><path d="M1 5h16l-2 8H3z" fill="none" stroke="#fff" stroke-width="1.5"/><path d="M5 5l4-4 4 4" fill="none" stroke="#fff" stroke-width="1.5"/></svg></div><div class="label">Shopping Cart<br>Item (0)</div></div>
    <nav class="abs nav"><span class="active">Home</span><span>About us</span><span>Bargain Corner</span><span>Online Store</span><span>Our Products</span><span>Contact Us</span></nav>
  </header>

  <section>
    <div class="abs tile" style="left:48px;top:146px;width:173px;height:277px;background:linear-gradient(#c9bfa8,#e8e2d2 60%,#b9a98b)" role="img" aria-label="Dining room with cream sofa by tall windows"><span class="tag">Dining Room</span></div>
    <div class="abs tile" style="left:222px;top:146px;width:341px;height:277px;background:linear-gradient(160deg,#5a2a1a,#2a1208 70%,#1a0a05)" role="img" aria-label="Three guests seated on a leather chesterfield sofa"></div>
    <div class="abs hero-caption">Lorem ipsum dolor sit amet consec</div>
    <div class="abs dots"><span></span><span></span><span></span><span></span><span></span></div>
    <div class="abs tile" style="left:564px;top:146px;width:173px;height:277px;background:linear-gradient(#e6e2dc,#cfc8bd 50%,#8a2020)" role="img" aria-label="Kitchen with red leather bar stools"><span class="tag">Kicthen</span></div>
    <div class="abs tile" style="left:48px;top:424px;width:173px;height:102px;background:linear-gradient(#8a8275,#c9ab7e 55%,#5c564e)" role="img" aria-label="Pine log coffee table on gravel"><span class="tag" style="top:39px">Living Room</span></div>
    <div class="abs tile" style="left:222px;top:424px;width:341px;height:102px;background:linear-gradient(90deg,#5b2a0e,#7a4220 60%,#c9b49a)" role="img" aria-label="Ornate white armchair on a brown backdrop"></div>
    <div class="abs promo"><h3>Free Shipping<br>On Order over $ 999</h3><p>This offers valid on all &nbsp;our store</p></div>
    <div class="abs tile" style="left:564px;top:424px;width:173px;height:102px;background:linear-gradient(#aab9c6,#7f9a6a 45%,#5f8a3a)" role="img" aria-label="Log beds on a grassy meadow"><span class="tag" style="top:14px">Bed Room</span></div>
  </section>

  <aside>
    <div class="abs" style="left:48px;top:548px"><h2 class="heading">Categories</h2><div class="rule"></div></div>
    <div class="abs search"><svg width="9" height="9" viewBox="0 0 9 9"><circle cx="3.5" cy="3.5" r="2.7" fill="none" stroke="#000" stroke-width="1.3"/><path d="M5.5 5.5L8.5 8.5" stroke="#000" stroke-width="1.5"/></svg>Search by items</div>
    <ul class="abs cats">
      <li>Bed Room</li><li>Kicthen</li><li>Living Room</li><li>Bedroom</li><li>Kitchen</li><li>Office Room</li><li>Bar Room</li><li>Outdorr</li><li>Lighting</li><li>Wall Decor</li><li>Fine Art Gallery</li><li>Accessories</li><li>Bargain Corner</li>
    </ul>
  </aside>

  <main>
    <div class="abs" style="left:233px;top:550px"><h2 class="heading">Welcome to Our Website</h2><div class="rule" style="width:111px"></div></div>
    <div class="abs intro">
      <div class="lead">Curabitur fringilla convallis interdumn auctorer oremnec empor nulla venenatiseu.</div>
      <p>Lorem ipsum dolor sit amet, consectetur adipiscing elit. Nullam vitae mi dolor. Morbi id purus in leo dictum imperdiet ac a sem. Praesent eu sagittis mi. Proin suscipit augue vitae felis gravida ultrices. Nulla ultrices congue laoreet.</p>
      <p style="margin-top:7px">Mauris vitae nisi scelerisque urna porttitor imperdiet.</p>
      <span class="btn" style="margin-top:9px">Read More</span>
    </div>
    <div class="abs" style="left:233px;top:698px"><h2 class="heading">Featured Products</h2><div class="rule" style="width:111px"></div></div>

    <div class="abs card first" style="left:233px">
      <div class="photo" style="background:linear-gradient(#3a3a3e,#4a3428 60%,#2a1d16);display:flex;align-items:center;justify-content:center" role="img" aria-label="Rustic wooden dresser"><svg width="18" height="18" viewBox="0 0 18 18"><circle cx="7" cy="7" r="5" fill="none" stroke="#fff" stroke-width="2.5"/><path d="M11 11l5 5" stroke="#fff" stroke-width="3"/></svg></div>
      <h4>Dressers</h4><p>Lorem ipsum dolor sit amet<br>Nullam vitae mi dolor Morbi id</p><span class="btn">Add To Cart</span>
    </div>
    <div class="abs card" style="left:406px">
      <div class="photo" style="background:linear-gradient(#6b6a66,#a0582a 50%,#4a3a2e)" role="img" aria-label="Burl wood dining table with chairs"></div>
      <h4>Bargin Corner</h4><p>Lorem ipsum dolor sit amet<br>Nullam vitae mi dolor Morbi id</p><span class="btn grey">Add To Cart</span>
    </div>
    <div class="abs card" style="left:578px">
      <div class="photo" style="background:linear-gradient(#7f8a4a,#c99a5a 45%,#6f7a3e)" role="img" aria-label="Half-log bench on grass"></div>
      <h4>Beanches</h4><p>Lorem ipsum dolor sit amet<br>Nullam vitae mi dolor Morbi id</p><span class="btn grey">Add To Cart</span>
    </div>
  </main>

  <footer class="abs footer"></footer>
  <div class="abs fcol" style="left:49px"><h5>What we like about....</h5><div class="rule"></div><ul><li class="on">Home</li><li>Our Meats</li><li>Family Farms</li><li>Our Bistro</li><li>Delivering to Your Door</li><li>Referral Program</li></ul></div>
  <div class="abs fcol" style="left:215px"><h5>My Account...</h5><div class="rule"></div><ul><li>Customer Services</li><li>Find Location</li><li>Our Store</li><li>Site map</li><li>Policy Privacy</li><li>Check Out</li></ul></div>
  <div class="abs fcol" style="left:350px"><h5>Our Products..</h5><div class="rule"></div><ul><li>Bed Room</li><li>Kicthen</li><li>Livinng Room</li><li>Office/Bar Room</li><li>Lighting</li><li>Wall decor</li></ul></div>
  <div class="abs fcol" style="left:480px"><h5>For Business..</h5><div class="rule"></div><ul><li>Nulla accumsan</li><li>Massachusetts</li><li>Fusce rhoncus</li><li>Pellentesque m</li><li>Maecenaspulv</li><li>Libero venenatis</li></ul></div>
  <div class="abs fcol" style="left:604px"><h5>Get Connect With Us</h5><div class="rule"></div>
    <div class="social"><span></span><span></span><span></span><span></span><span></span></div>
    <h5 style="margin-top:26px">Contact Us</h5><div class="rule"></div>
    <div class="fcontact" style="margin-top:8px"><b>Tel:</b> 555 014 2290<br><b>Fax:</b> 555 014 2290<br><b>Email:</b> mail@birchandember.example</div>
  </div>
  <div class="abs copy">© 2014 Birch &amp; Ember &nbsp;All rights reserved.</div>
</div>
</body>
</html>
```